Lawn Sign Design – Brisko

We need a clean, eye-catching 18" x 24" lawn sign for Brisko that effectively communicates our core message while maintaining strong brand consistency.

Key Elements to Include:
Tagline (Main Focus): Upgrade Your Roof Without Replacing It
Website: www.tryvexlo-demo.example
Phone Number: (877) BRISKO-GO
RQMH License Number: 4830516
Brisko Logo & Branding: Ensure the logo, corporate colors, and custom font are used consistently to align with our existing branding.

Design Guidelines:
Simple & High-Impact: The tagline should be the most prominent element on the sign, drawing immediate attention.
Easy Readability: Use a bold, clean design with high contrast for quick readability from a distance.
Balanced Layout: Place supporting details (website, phone number, and RQMH number) in a visually clear but secondary position to the tagline.
Professional & Modern: The sign should reflect credibility and innovation in the roofing industry.

Deliverables:
High-resolution print-ready files (CMYK)
A digital proof for review before finalizing
The final design should make a strong impression with minimal text, ensuring that anyone passing by can instantly grasp what we offer.

I am including our custom font. To get an hexagon in our name, simply type the $ after the 'O" Please use this font for anything you type.

```html
<!DOCTYPE html>
<html lang="en">
<head>
<meta charset="utf-8">
<title>Brisko Lawn Sign</title>
<link href="https://fonts.googleapis.com/css2?family=Montserrat:wght@500;600;700&display=swap" rel="stylesheet">
<style>
  :root {
    --brand-blue: #12529b;
    --brand-blue-deep: #0f4789;
    --sign-white: #ffffff;
    --backdrop: #e9ecef;
  }
  * { margin: 0; padding: 0; box-sizing: border-box; }
  html, body {
    width: 1200px;
    height: 900px;
    overflow: hidden;
    background: var(--backdrop);
    font-family: "Montserrat", Arial, sans-serif;
  }
  .lawn-sign {
    position: absolute;
    left: 60px;
    top: 90px;
    width: 1080px;
    height: 720px;
    background: var(--sign-white);
    overflow: hidden;
    box-shadow: 0 6px 24px rgba(0,0,0,0.12);
  }
  .accent-panel {
    position: absolute;
    top: 0;
    right: 0;
    width: 250px;
    height: 100%;
    background: linear-gradient(180deg, var(--brand-blue) 0%, var(--brand-blue-deep) 100%);
  }
  .brand-mark {
    position: absolute;
    left: 266px;
    top: 86px;
    width: 172px;
    height: 172px;
    background: var(--brand-blue);
  }
  .brand-name {
    position: absolute;
    left: 72px;
    top: 325px;
    font-size: 123px;
    font-weight: 700;
    letter-spacing: 8px;
    color: var(--brand-blue);
    line-height: 1;
  }
  .contact {
    position: absolute;
    left: 75px;
    color: var(--brand-blue);
    line-height: 1;
    white-space: nowrap;
  }
  .contact-web { top: 470px; font-size: 34px; font-weight: 600; }
  .contact-phone { top: 515px; font-size: 57px; font-weight: 700; }
  .contact-license { top: 582px; font-size: 36px; font-weight: 500; }
  .tagline { top: 648px; font-size: 33px; font-weight: 700; letter-spacing: 0.2px; }
</style>
</head>
<body>
  <div class="lawn-sign">
    <div class="accent-panel" role="img" aria-label="Decorative brand-blue accent area"></div>
    <div class="brand-mark"></div>
    <div class="brand-name">BRISKO</div>
    <p class="contact contact-web">www.tryvexlo-demo.example</p>
    <p class="contact contact-phone">Tel : (877) BRISKO-GO</p>
    <p class="contact contact-license">RQMH License Number: 4830516</p>
    <p class="contact tagline">Upgrade Your Roof Without Replacing It</p>
  </div>
</body>
</html>
```